Kitchen and bathroom exhaust fan cleaning business card design

A new business cleaning domestic - not commercial - exhaust/extractor fans in kitchens, bathrooms and en suites and kitchen range hood filters.

We would like a bright colour suggesting cleanliness (such a syellow or light green?)

I would like to see on the card preferably on the reverse:

"We clean kitchen and bathroom exhaust fans & Vormo Heatlites
and
clean and repair range hood filters and replace carbon filters

We give Pensioner discounts

Designers pls note the TM in the contact filed after Brisko Airworks should be superscript as in the trademark sign. On the reverse of the card, I would like:: "We clean kitchen and bathroom exhaust fans & Vormo Heatlites & clean and repair range hood filters and replace carbon filters We give Pensioner discounts

Reason: I will be out of the country for several days

Target Market(s)

people who are too lazy or too busy to clean their fan units and pensioners and others who are unable to do it.

Industry/Entity Type

Business

Contact Information for Business Card

Brisko AirworksTM Designer pls note the TM should be superscript as in the trademark sign
Alan Petworth
Mob: 0491 570 263
Email: briskoairworks@postlume.net
PO Box 7152, Hawker ACT 2614

Requirements
Must have
• Designer pls note the TM in the contact filed after Brisko Airworks should be superscript as in the trademark sign.

On the reverse

and

```html
<!DOCTYPE html>
<html lang="en">
<head>
<meta charset="utf-8">
<title>Brisko Airworks – Business Card</title>
<link rel="stylesheet" href="https://fonts.googleapis.com/css2?family=Marcellus&family=Exo+2:wght@400;600&display=swap">
<style>
  :root {
    --backdrop: #dcdcde;
    --card-white: #fbfbfc;
    --brand-navy: #3c3c93;
    --brand-sky: #1fb2ea;
    --ink-grey: #3a3a44;
    --on-navy: #ffffff;
  }
  * { margin: 0; padding: 0; box-sizing: border-box; }
  html, body {
    width: 1200px; height: 900px; overflow: hidden;
    background: var(--backdrop);
  }
  .canvas {
    position: relative; width: 1200px; height: 900px;
    display: flex; align-items: center; justify-content: center;
  }
  .business-card {
    position: relative; width: 1000px; height: 572px;
    background: var(--card-white);
    box-shadow: 0 18px 40px rgba(0,0,0,0.18);
    overflow: hidden;
  }
  .card-artwork { position: absolute; inset: 0; width: 100%; height: 100%; }
  .wordmark {
    position: absolute; left: 80px; top: 80px;
    font-family: "Marcellus", serif; font-weight: 400; color: var(--brand-navy);
    line-height: 1; letter-spacing: 2px;
  }
  .wordmark .line-one { display: block; font-size: 88px; }
  .wordmark .line-two { display: block; font-size: 54px; margin-top: 6px; }
  .wordmark sup { font-size: 20px; vertical-align: super; letter-spacing: 0; }
  .holder {
    position: absolute; left: 170px; top: 318px;
    font-family: "Exo 2", sans-serif;
  }
  .holder-name {
    font-size: 30px; font-weight: 600; letter-spacing: 3px;
    color: var(--brand-navy);
  }
  .holder-role {
    font-size: 23px; font-weight: 400; letter-spacing: 1.5px;
    color: var(--ink-grey); margin-left: 28px;
  }
  .contact-list {
    position: absolute; right: 36px; top: 90px;
    list-style: none; text-align: right;
    font-family: "Exo 2", sans-serif; color: var(--on-navy);
    font-size: 16px; letter-spacing: 1px; line-height: 1.55;
  }
  .contact-list li { display: flex; justify-content: flex-end; align-items: center; gap: 10px; }
  .contact-list .address { margin-bottom: 16px; font-size: 17px; line-height: 1.4; }
  .contact-icon { width: 14px; height: 14px; flex: none; }
</style>
</head>
<body>
<main class="canvas">
  <article class="business-card">
    <svg class="card-artwork" viewBox="0 0 1000 572" aria-hidden="true">
      <path d="M620 0 C720 300 600 470 80 572 L1000 572 L1000 0 Z" fill="var(--brand-navy)"/>
      <path d="M608 60 C712 300 588 468 50 572 L10 572 C565 460 690 300 608 60 Z" fill="var(--brand-sky)"/>
    </svg>

    <h1 class="wordmark">
      <span class="line-one">Brisko</span>
      <span class="line-two">AIRWORKS<sup>TM</sup></span>
    </h1>

    <div class="holder">
      <p class="holder-name">ALAN PETWORTH</p>
      <p class="holder-role">Managing Director</p>
    </div>

    <ul class="contact-list">
      <li class="address">PO Box 7152,<br>Hawker ACT 2614</li>
      <li>0491 570 263
        <svg class="contact-icon" viewBox="0 0 14 14"><path d="M3 1 L5 4 L4 5.5 C5 7.5 6.5 9 8.5 10 L10 9 L13 11 L11.5 13 C6 12.5 1.5 8 1 2.5 Z" fill="currentColor"/></svg>
      </li>
      <li>0491 570 263
        <svg class="contact-icon" viewBox="0 0 14 14"><rect x="3.5" y="1" width="7" height="12" rx="1.5" fill="none" stroke="currentColor" stroke-width="1.5"/><circle cx="7" cy="10.5" r="0.9" fill="currentColor"/></svg>
      </li>
      <li>0491 570 263
        <svg class="contact-icon" viewBox="0 0 14 14"><rect x="1" y="5" width="12" height="7" rx="1" fill="currentColor"/><rect x="4" y="1.5" width="6" height="4" fill="currentColor"/></svg>
      </li>
      <li>briskoairworks@postlume.net
        <svg class="contact-icon" viewBox="0 0 14 14"><rect x="1" y="3" width="12" height="8.5" rx="1" fill="currentColor"/><path d="M1.5 3.5 L7 8 L12.5 3.5" fill="none" stroke="var(--brand-navy)" stroke-width="1.2"/></svg>
      </li>
      <li>www.briskoairworks.net
        <svg class="contact-icon" viewBox="0 0 14 14"><circle cx="7" cy="7" r="6" fill="currentColor"/><ellipse cx="7" cy="7" rx="2.5" ry="6" fill="none" stroke="var(--brand-navy)" stroke-width="1"/><line x1="1" y1="7" x2="13" y2="7" stroke="var(--brand-navy)" stroke-width="1"/></svg>
      </li>
    </ul>
  </article>
</main>
</body>
</html>
```